I am looking for a book cover designs. The title of the book is "Ways to stand out and where your habits slip"

the book is not too formal but it is also not informal.

I wish for the title to be easily readable and capturing, especially the "ways to stand out" part.

the book should also include the author name: Tobar Kessly

everyone

• Full title and author name: Tobar Kessly
• There is a chapter that is called "turn the lamp inward", if you wish to do an illustration as part of the cover then perhaps that can give you an idea of what to go with.
• anything that takes attention away from the title.Also should not include any photographs.

```html
<!DOCTYPE html>
<html lang="en">
<head>
<meta charset="utf-8">
<title>Ways to Stand Out — Tobar Kessly</title>
<link rel="stylesheet" href="https://fonts.googleapis.com/css2?family=Anton&family=Oswald:wght@600;700&display=swap">
<style>
  :root {
    --paper-light: #fbfbfb;
    --paper-shade: #d9d9d9;
    --ink: #141414;
    --accent-red: #e3191b;
    --band-black: #111111;
    --tear-edge: #bdbdbd;
    --band-text: #ffffff;
  }
  * { margin: 0; padding: 0; box-sizing: border-box; }
  html, body {
    width: 769px;
    height: 1200px;
    overflow: hidden;
    background: var(--paper-shade);
  }
  .cover {
    position: relative;
    width: 769px;
    height: 1200px;
    overflow: hidden;
    background: radial-gradient(ellipse at 50% 40%, var(--paper-light) 0%, #efefef 55%, var(--paper-shade) 100%);
  }
  .emblem {
    position: absolute;
    left: 50%;
    top: 44px;
    width: 78px;
    height: 74px;
    transform: translateX(-50%);
    border-radius: 10px;
    background: var(--ink);
  }
  .title {
    position: absolute;
    left: 0;
    right: 0;
    top: 150px;
    text-align: center;
    font-family: "Anton", "Oswald", sans-serif;
    color: var(--accent-red);
    text-transform: uppercase;
    font-size: 152px;
    line-height: 146px;
    letter-spacing: 1px;
  }
  .band {
    position: absolute;
    left: 0;
    top: 480px;
    width: 769px;
    height: 530px;
  }
  .band svg { display: block; width: 100%; height: 100%; }
  .subtitle {
    position: absolute;
    left: 0;
    right: 0;
    top: 594px;
    text-align: center;
    font-family: "Oswald", sans-serif;
    font-weight: 700;
    font-size: 52px;
    line-height: 60px;
    color: var(--band-text);
    text-transform: uppercase;
    letter-spacing: 0.5px;
  }
  .subtitle-key {
    position: absolute;
    left: 0;
    right: 0;
    top: 664px;
    text-align: center;
    font-family: "Anton", sans-serif;
    font-size: 158px;
    line-height: 170px;
    color: var(--accent-red);
    text-transform: uppercase;
    letter-spacing: 3px;
  }
  .author {
    position: absolute;
    left: 0;
    right: 0;
    top: 1022px;
    text-align: center;
    font-family: "Oswald", sans-serif;
    font-weight: 700;
    font-size: 88px;
    line-height: 96px;
    color: var(--ink);
    text-transform: uppercase;
    letter-spacing: 2px;
  }
</style>
</head>
<body>
  <main class="cover">
    <div class="emblem" role="img" aria-label="Small black icon of a seated figure meditating in a floating pose"></div>

    <h1 class="title">Ways to<br>Stand Out</h1>

    <div class="band" aria-hidden="true">
      <svg viewBox="0 0 769 530" preserveAspectRatio="none">
        <polygon fill="var(--tear-edge)" points="0,14 40,8 72,18 110,6 150,16 196,4 238,14 280,7 326,18 370,5 410,15 452,8 498,19 540,6 584,16 626,5 668,17 712,8 769,15 769,522 724,512 680,524 636,513 590,525 546,512 500,523 456,511 410,524 364,512 318,525 272,513 226,524 180,511 134,523 88,512 44,524 0,514"/>
        <polygon fill="var(--band-black)" points="0,24 46,18 82,28 120,17 162,27 204,15 246,26 290,18 334,29 378,16 420,27 462,19 506,29 548,17 592,27 634,16 676,28 720,19 769,26 769,508 726,500 684,511 638,501 594,512 550,500 504,510 460,499 414,511 368,500 322,512 276,501 230,511 184,499 138,510 92,500 46,511 0,502"/>
      </svg>
    </div>

    <p class="subtitle">And where your habits</p>
    <p class="subtitle-key">Slip</p>

    <p class="author">Tobar Kessly</p>
  </main>
</body>
</html>
```